Crisp meadow hair . Need to be noticed small town with 15 other salons which are all clinical clean

Hair salon, modern industrial look, new image face lift, been an established salon for 35+ years was extremely dated (80s) need to be known as successful fresh look salon.
All aspects of hair- ladies mens and children, style cuts, basic - fashion colour work, blowdry, Upstyling, perming, hair treatments, professional color and retail. Specialising staff for color and cuts. Staff ages young and funky to mature

Reason: Would like some more variety of design

Target Market(s)

Walk by traffic, new clients, to be seen

Industry/Entity Type

Hair

Font styles to use
Sans Serif

Requirements
Must have
• Crisp meadow hair
Nice to have
• Timber look, brick
Should not have
• Pretty (floral, script writing , pictures of sissors or combs or brushes)

```html
<!DOCTYPE html>
<html lang="en">
<head>
<meta charset="utf-8">
<title>Crisp Meadow Hair – Shopfront</title>
<link rel="stylesheet" href="https://fonts.googleapis.com/css2?family=Oswald:wght@400;500;600&display=swap">
<style>
  :root {
    --page: #ffffff;
    --ink: #0a0a0a;
    --paper: #ffffff;
    --timber-light: #f1d3ad;
    --timber-mid: #e6bf92;
    --timber-dark: #d8a978;
    --interior-dark: #1e1a17;
    --interior-warm: #8a6a48;
    --interior-glow: #d9b98e;
    --interior-bright: #efe6d8;
  }
  html, body {
    margin: 0;
    padding: 0;
    width: 1200px;
    height: 849px;
    overflow: hidden;
    background: var(--page);
  }
  .shopfront {
    position: relative;
    width: 1200px;
    height: 849px;
    font-family: "Oswald", "Arial Narrow", sans-serif;
    color: var(--paper);
  }
  .timber {
    position: absolute;
    background: linear-gradient(100deg, var(--timber-light), var(--timber-mid) 50%, var(--timber-light) 80%, var(--timber-dark));
  }
  .timber--fascia { left: 40px; top: 180px; width: 1063px; height: 112px; }
  .timber--pillar-left { left: 40px; top: 292px; width: 62px; height: 313px; }
  .timber--pillar-mid { left: 470px; top: 292px; width: 85px; height: 313px; }
  .timber--pillar-right { left: 978px; top: 292px; width: 84px; height: 306px; }

  .window {
    position: absolute;
    overflow: hidden;
  }
  .window--left {
    left: 102px; top: 292px; width: 368px; height: 313px;
    background: linear-gradient(90deg, var(--interior-dark) 0%, var(--interior-warm) 25%, var(--interior-glow) 45%, var(--interior-warm) 65%, var(--interior-dark) 100%);
  }
  .window--right {
    left: 555px; top: 292px; width: 423px; height: 306px;
    background: linear-gradient(90deg, var(--interior-warm) 0%, var(--interior-glow) 20%, var(--interior-bright) 45%, var(--interior-glow) 70%, var(--interior-bright) 100%);
  }

  .window__band {
    position: absolute;
    left: 0; top: 0; right: 0;
    height: 66px;
    background: var(--ink);
  }
  .window__label {
    position: absolute;
    top: 25px;
    left: 7px;
    font-size: 16px;
    font-weight: 500;
    letter-spacing: 0.2px;
  }
  .window--right .window__label { left: 10px; }

  .stripes {
    position: absolute;
    left: 0; top: 0;
    width: 1200px; height: 849px;
    pointer-events: none;
  }

  .sign-band {
    position: absolute;
    left: 470px; top: 205px;
    width: 633px; height: 60px;
    background: var(--ink);
  }
  .sign-band__mark {
    position: absolute;
    left: 70px; top: 6px;
    width: 130px;
    text-align: center;
    font-size: 20px;
    font-weight: 600;
    line-height: 24px;
    text-transform: uppercase;
  }
  .sign-band__name {
    position: absolute;
    left: 250px; top: 2px;
    margin: 0;
    font-size: 39px;
    font-weight: 600;
    line-height: 56px;
    letter-spacing: 0.3px;
    white-space: nowrap;
  }

  .pillar-panel {
    position: absolute;
    left: 481px; top: 362px;
    width: 60px; height: 216px;
    background: var(--ink);
    text-align: center;
  }
  .pillar-panel__name {
    display: block;
    margin-top: 8px;
    font-size: 12px;
    font-weight: 600;
    line-height: 13px;
    text-transform: uppercase;
  }
  .services {
    list-style: none;
    margin: 36px 0 0;
    padding: 0;
    font-size: 9px;
    font-weight: 500;
    line-height: 14px;
  }

  .walk-ins {
    position: absolute;
    left: 102px; top: 460px;
    width: 170px; height: 135px;
    text-align: center;
  }
  .walk-ins__shape { position: absolute; left: 0; top: 0; }
  .walk-ins__text { position: relative; margin: 0; padding-top: 18px; }
  .walk-ins__yes {
    display: block;
    font-size: 42px;
    font-weight: 600;
    line-height: 46px;
    margin-left: -20px;
  }
  .walk-ins__line {
    display: block;
    font-size: 19px;
    font-weight: 500;
    line-height: 22px;
    margin-left: -8px;
  }
  .walk-ins__who {
    display: block;
    font-size: 11px;
    font-weight: 500;
    line-height: 16px;
    margin-left: -8px;
  }
</style>
</head>
<body>
<main class="shopfront">
  <div class="timber timber--fascia" role="img" aria-label="Timber-look cladding"></div>
  <div class="timber timber--pillar-left" role="img" aria-label="Timber-look cladding"></div>
  <div class="timber timber--pillar-mid" role="img" aria-label="Timber-look cladding"></div>
  <div class="timber timber--pillar-right" role="img" aria-label="Timber-look cladding"></div>

  <section class="window window--left" role="img" aria-label="Salon interior seen through the window, styling stations with lit mirrors">
    <div class="window__band"><span class="window__label">www.crispmeadowhair.com</span></div>
  </section>
  <section class="window window--right" role="img" aria-label="Salon interior seen through the window, retail shelving and clients at stations">
    <div class="window__band"><span class="window__label">Call: 0000 000 000</span></div>
  </section>

  <svg class="stripes" viewBox="0 0 1200 849" aria-hidden="true">
    <polygon points="102,372 470,358 470,366 102,384" fill="#ffffff"/>
    <polygon points="555,376 978,355 978,366 555,391" fill="#ffffff"/>
  </svg>

  <header class="sign-band">
    <span class="sign-band__mark">Crisp<br>Meadow</span>
    <h1 class="sign-band__name">Crisp Meadow Hair</h1>
  </header>

  <aside class="pillar-panel">
    <span class="pillar-panel__name">Crisp<br>Meadow</span>
    <ul class="services">
      <li>Ladies</li>
      <li>Men</li>
      <li>Children</li>
      <li>Styles</li>
      <li>Cut</li>
      <li>Colour</li>
      <li>Blowdry</li>
      <li>Upstyle</li>
      <li>Perm</li>
      <li>Treatment</li>
    </ul>
  </aside>

  <div class="walk-ins">
    <svg class="walk-ins__shape" width="170" height="135" viewBox="0 0 170 135" aria-hidden="true">
      <polygon points="0,68 62,0 112,0 170,68 112,135 0,135" fill="#0a0a0a"/>
    </svg>
    <p class="walk-ins__text">
      <span class="walk-ins__yes">Yes</span>
      <span class="walk-ins__line">we take walk in’s</span>
      <span class="walk-ins__who">men - women - children</span>
    </p>
  </div>
</main>
</body>
</html>
```